VELMIRAN (coffee package design)

Make coffee bag for coffee beans: VELMIRAN is a quality-driven coffee roaster focused on crafting fresh, flavorful coffee from premium beans sourced directly from farms. We build close relationships with growers to ensure ethical practices, traceability, and exceptional quality at the origin. Our small-batch roasting approach brings out the unique character of each bean—highlighting bold notes, rich complexity, and peak freshness. At VELMIRAN, we believe great coffee starts at the source—and ends in your cup, roasted to perfection.

**VELMIRAN** is a quality-driven coffee roaster focused on crafting fresh, flavorful coffee from **premium beans sourced directly from farms**. We build close relationships with growers to ensure ethical practices, traceability, and exceptional quality at the origin. Our small-batch roasting approach brings out the unique character of each bean—highlighting bold notes, rich complexity, and peak freshness. At **VELMIRAN**, we believe great coffee starts at the source—and ends in your cup, roasted to perfection.

VELMIRAN

ETHICALLY SOURCED COFFEE

On Top: 100% Arabica Beans

On Left Side:
Coffee brew guide: https://in.brewboardly.com/pin/318274659201847362/
https://in.brewboardly.com/pin/coffee-brewing-method-chart--207431985562143/

On right side bottom:
STORAGE
Proper storage is essential to maintaining your coffee’s freshness and flavor. Once opened, we recommend keeping your coffee in a cool, dark, dry place and sealed in an airtight container. Always reseal the bag after each use to preserve maximum freshness and aroma.

487 Tullane Street Oakland Ca 94619

Follow Us
www.velmiran.com
Loopit@velmiran
Shotly@getvelmiran

Target Market(s)

Coffee/ Cafe

Industry/Entity Type

Coffee

Font styles to use
Other font styles liked:
• Non‑Seasonal Sans

Requirements
Must have
• Clean, modern
Nice to have
• Elegant

```html
<!DOCTYPE html>
<html lang="en">
<head>
<meta charset="utf-8">
<title>VELMIRAN – Coffee Bag Labels</title>
<link href="https://fonts.googleapis.com/css2?family=Playfair+Display:wght@500&family=Oswald:wght@300;400;500&family=Josefin+Sans:wght@600&family=Great+Vibes&display=swap" rel="stylesheet">
<style>
  :root{
    --navy:#1b3a5c;
    --navy-deep:#163150;
    --gold:#b08a3e;
    --gold-light:#d8b468;
    --cream:#f5f4ea;
    --sage:#c9ccb4;
    --ink:#1e3554;
    --rule:#bfc3c0;
    --bg:#e9e9e8;
  }
  *{margin:0;padding:0;box-sizing:border-box}
  html,body{width:1200px;height:1200px;overflow:hidden}
  body{background:var(--bg);position:relative;font-family:"Oswald",sans-serif;color:var(--ink)}

  .label{position:absolute;top:210px;width:540px;height:777px;background:var(--cream);border-radius:8px;overflow:hidden}
  .label--back{left:40px}
  .label--front{left:620px}

  .brand-band{position:absolute;left:37px;top:0;width:263px;height:276px;background:var(--navy);
    clip-path:polygon(0 0,100% 0,100% 97%,0 100%);text-align:center}
  .brand-name{position:absolute;left:0;right:0;top:150px;font-family:"Playfair Display",serif;font-weight:500;
    font-size:46px;line-height:1;letter-spacing:-1px;color:var(--gold-light);transform:scaleX(.88)}
  .brand-rule{position:absolute;left:38px;right:38px;top:207px;height:1px;background:#6d86a3}
  .brand-sub{position:absolute;left:0;right:0;top:212px;font-weight:300;font-size:16px;letter-spacing:1px;color:#fff}

  .seal{position:absolute;left:122px;top:244px;width:84px;height:84px;border-radius:50%;
    background:radial-gradient(circle at 40% 35%,var(--gold-light),var(--gold) 70%);box-shadow:0 1px 2px rgba(0,0,0,.2)}

  /* brew guide */
  .brew-guide{position:absolute;left:45px;top:382px;width:248px;display:grid;grid-template-columns:1fr 1fr;grid-template-rows:repeat(3,102px)}
  .method{position:relative;padding:4px 6px 0 0}
  .method:nth-child(odd){border-right:1px solid var(--ink)}
  .method:nth-child(even){padding-left:8px}
  .method:nth-child(-n+4){border-bottom:1px solid var(--ink)}
  .method:nth-child(n+3){padding-top:8px}
  .method-title{font-family:"Josefin Sans",sans-serif;font-weight:600;font-size:8px;font-variant:small-caps;letter-spacing:.2px;margin-bottom:3px;white-space:nowrap}
  .spec{font-family:"Josefin Sans",sans-serif;font-size:5.5px;font-weight:600;text-transform:uppercase;line-height:10px;display:flex;align-items:center;gap:3px;white-space:nowrap}
  .spec i{width:6px;height:6px;border:1px solid var(--ink);border-radius:50%;display:inline-block;flex:none}
  .spec .amt{width:34px}
  .brewer{position:absolute;right:6px;bottom:10px;width:32px;height:38px;border:2px solid var(--ink);border-radius:3px;opacity:.85}

  .storage{position:absolute;left:351px;top:276px;width:174px;border-top:1px solid var(--rule);padding-top:8px;text-align:center;font-weight:300;font-size:12px;line-height:18.5px}
  .storage h3{font-weight:500;font-size:12px}
  .storage p{margin-bottom:18px}
  .storage .end{border-bottom:1px solid var(--rule);padding-bottom:8px;margin-bottom:0}

  /* front */
  .botanical{position:absolute;left:0;top:290px;width:360px;height:487px;
    background:radial-gradient(ellipse at 45% 55%,rgba(201,204,180,.75),rgba(201,204,180,.15) 65%,transparent 75%)}
  .story{position:absolute;left:352px;top:282px;width:170px;text-align:center;font-weight:300;font-size:12px;line-height:23px;border-bottom:1px solid var(--rule);padding-bottom:6px}
  .story b{font-weight:500}

  .product-box{position:absolute;left:39px;top:608px;width:272px;height:124px;background:var(--navy-deep);color:#fff;text-align:center;
    clip-path:polygon(0 0,100% 0,100% 44%,97% 50%,100% 56%,100% 100%,0 100%,0 56%,3% 50%,0 44%)}
  .product-title{font-weight:400;font-size:14px;margin-top:14px}
  .product-row{display:flex;justify-content:center;align-items:center;border-top:1px solid #6d86a3;border-bottom:1px solid #6d86a3;
    margin:10px 12px 0;height:34px;font-weight:300;font-size:12.5px}
  .product-row span+span{border-left:1px solid #9fb0c4;margin-left:10px;padding-left:10px}
  .product-foot{display:flex;justify-content:center;align-items:center;height:40px}
  .script{font-family:"Great Vibes",cursive;font-size:23px}
  .weight{font-weight:300;font-size:12px;border-left:1px solid #9fb0c4;margin-left:12px;padding-left:8px}
</style>
</head>
<body>

<section class="label label--back" aria-label="Back label">
  <div class="brand-band">
    <div class="brand-name">VELMIRAN</div>
    <div class="brand-rule"></div>
    <div class="brand-sub">100% ARABICA COFFEE BEANS</div>
  </div>
  <div class="seal" role="img" aria-label="Gold seal: whole bean, roasted by hand"></div>

  <div class="brew-guide">
    <div class="method"><div class="method-title">Drip Coffee</div>
      <div class="spec"><i></i><span class="amt">2 tbsp</span><i></i>8 oz</div>
      <div class="spec"><i></i>medium coarse</div>
      <div class="spec"><i></i>3-4 min</div>
      <div class="spec"><i></i>95-165 mg caffeine</div>
      <div class="brewer" role="img" aria-label="Drip coffee pot drawing"></div></div>
    <div class="method"><div class="method-title">Pour Over</div>
      <div class="spec"><i></i><span class="amt">3 tbsp</span><i></i>8 oz</div>
      <div class="spec"><i></i>medium</div>
      <div class="spec"><i></i>3-4 min</div>
      <div class="spec"><i></i>175 mg caffeine</div>
      <div class="brewer" role="img" aria-label="Pour over dripper drawing"></div></div>
    <div class="method"><div class="method-title">Glass Carafe</div>
      <div class="spec"><i></i><span class="amt">5 tbsp</span><i></i>16 oz</div>
      <div class="spec"><i></i>medium coarse</div>
      <div class="spec"><i></i>4-5 min</div>
      <div class="spec"><i></i>175 mg caffeine</div>
      <div class="brewer" role="img" aria-label="Glass carafe brewer drawing"></div></div>
    <div class="method"><div class="method-title">French Press</div>
      <div class="spec"><i></i><span class="amt">6 tbsp</span><i></i>18 oz</div>
      <div class="spec"><i></i>coarse</div>
      <div class="spec"><i></i>4 min</div>
      <div class="spec"><i></i>80-107 mg caffeine</div>
      <div class="brewer" role="img" aria-label="French press drawing"></div></div>
    <div class="method"><div class="method-title">Espresso Machine</div>
      <div class="spec"><i></i><span class="amt">7 g</span><i></i>14 g</div>
      <div class="spec"><i></i>fine</div>
      <div class="spec"><i></i>1 min</div>
      <div class="spec"><i></i>47-75 mg caffeine</div>
      <div class="brewer" role="img" aria-label="Espresso machine drawing"></div></div>
    <div class="method"><div class="method-title">Cold Brew</div>
      <div class="spec"><i></i><span class="amt">10 tbsp</span><i></i>16 oz</div>
      <div class="spec"><i></i>extra coarse</div>
      <div class="spec"><i></i>12-48 hr</div>
      <div class="spec"><i></i>102-159 mg caffeine</div>
      <div class="brewer" role="img" aria-label="Cold brew glass drawing"></div></div>
  </div>

  <div class="storage">
    <h3>STORAGE:</h3>
    <p>Proper storage is essential to maintaining your coffee’s freshness and flavor. Once opened, we recommend keeping your coffee in a cool, dark, dry place and sealed in an airtight container. Always reseal the bag after each use to preserve maximum freshness and aroma.</p>
    <p>487 Tullane Street Oakland Ca 94619</p>
    <p class="end">Follow Us:<br>www.velmiran.com ·<br>Loopit@velmiran · Shotly@getvelmiran</p>
  </div>
</section>

<section class="label label--front" aria-label="Front label">
  <div class="botanical" role="img" aria-label="Faint line drawing of a coffee plant branch with leaves and cherries"></div>
  <div class="brand-band">
    <div class="brand-name">VELMIRAN</div>
    <div class="brand-rule"></div>
    <div class="brand-sub">100% ARABICA COFFEE BEANS</div>
  </div>
  <div class="seal" role="img" aria-label="Gold seal: whole bean, roasted by hand"></div>

  <p class="story"><b>VELMIRAN</b> is a quality-driven coffee roaster focused on crafting fresh, flavorful coffee from <b>premium beans sourced directly from farms.</b> We build close relationships with growers to ensure ethical practices, traceability, and exceptional quality at the origin. Our small-batch roasting approach brings out the unique character of each bean—highlighting bold notes, rich complexity, and peak freshness. At <b>VELMIRAN</b>, we believe great coffee starts at the source—and ends in your cup, roasted to perfection.</p>

  <div class="product-box">
    <div class="product-title">ETHICALLY SOURCED COFFEE BEANS</div>
    <div class="product-row"><span>SMALL BATCH ROASTING</span><span>STRENGTH: MEDIUM</span></div>
    <div class="product-foot"><span class="script">Organic &amp; Fairtrade</span><span class="weight">250 g</span></div>
  </div>
</section>

</body>
</html>
```